Wordpress theme for food/recipe blog - family friendly

I've recently setup a Wordpress site to document all my tried and tested recipes. However I'm not happy with the design and layout of the theme I got. See brightspoonkit.com

It's also lacking a header/identity/logo as well. I would like a theme which is eye catching, cute and easy to navigate bearing in mind that the site is meant to be a personal blog documenting my culinary journey.

I would definitely like a logo / cartoon of a chubby, dimpled specky girl in apron perhaps holding up some utensil to show what this blog is about. I cook mainly for my family comprising my husband and our little baby girl who is 16months.

I love making breads the most if that helps with the logo/header design.
Updates

Reason: need more designs

Target Market(s)

- family with young kids
- mummies
- amateur cooks
- people who love food/ baking and cooking and sharing recipes

Industry/Entity Type

Baby

Requirements
Must have
• - Viewable on mobile - ie must be mobile friendly
- header/image - when shared on social media the image will be the one that is identified by people/readers

```html
<!DOCTYPE html>
<html lang="en">
<head>
<meta charset="utf-8">
<title>Bright Spoon Kitchen</title>
<link rel="stylesheet" href="https://fonts.googleapis.com/css2?family=Roboto+Condensed:wght@400;700&family=PT+Sans:ital,wght@0,400;0,700;1,400&display=swap">
<style>
:root{
  --red:#d71f36;
  --red-dark:#c21a2f;
  --nav-active:#4d5158;
  --text:#666a6e;
  --muted:#8a8d90;
  --rule:#d9d9d9;
  --white:#ffffff;
}
*{box-sizing:border-box;margin:0;padding:0}
html,body{width:993px;height:1200px;overflow:hidden;background:var(--white)}
body{position:relative;font-family:"PT Sans",sans-serif;color:var(--text)}
.abs{position:absolute}
.cond{font-family:"Roboto Condensed",sans-serif}

.brand{left:150px;top:10px;display:flex;align-items:center;gap:10px}
.brand-mark{width:50px;height:50px;border-radius:50%;background:#f3d7d6}
.brand-name{font-family:"Roboto Condensed",sans-serif;font-weight:700;font-size:30px;color:var(--red)}
.follow{right:150px;top:29px;display:flex;align-items:center;gap:4px;font-size:8.5px;color:#555}
.follow span{margin-right:4px}
.social{width:21px;height:21px;border-radius:50%;background:var(--nav-active)}
.social.alt{background:var(--red)}

.nav{left:0;top:77px;width:993px;height:37px;background:var(--red);border-bottom:1px solid var(--red-dark)}
.nav ul{list-style:none;position:absolute;left:149px;top:0;height:37px;display:flex}
.nav li{height:37px;line-height:37px;font-family:"Roboto Condensed",sans-serif;font-size:12px;color:var(--white);text-transform:uppercase}
.nav li.active{background:var(--nav-active);width:103px;text-align:center}
.nav li.item{position:absolute;white-space:nowrap}

.slider{left:150px;top:120px;width:695px;height:335px;background:radial-gradient(ellipse at 55% 50%,#6a3a26 0%,#a9733f 35%,#cdb38a 60%,#eeeeea 85%);box-shadow:0 8px 6px -4px rgba(0,0,0,.35)}
.slider-arrow{position:absolute;top:143px;width:48px;height:48px;background:rgba(220,120,130,.55)}
.slider-arrow.prev{left:0}.slider-arrow.next{right:0}
.slider-arrow svg{position:absolute;left:17px;top:14px}

.welcome-title{left:150px;top:488px;width:695px;text-align:center;font-size:27px;color:var(--red)}
.double-rule{left:150px;top:532px;width:695px;height:4px;border-top:2px solid var(--rule);border-bottom:1px solid var(--rule)}
.welcome-text{left:150px;top:553px;width:695px;text-align:center;font-size:9px;line-height:15.5px}

.section-title{font-family:"Roboto Condensed",sans-serif;color:var(--red);text-transform:uppercase}
.feature-title{left:150px;top:626px;width:695px;text-align:center;font-size:19px}
.pager{display:flex;gap:1px}
.pager i{display:block;width:25px;height:14px;background:var(--red);position:relative}
.pager svg{position:absolute;left:6px;top:4px}

.recipe{top:673px;width:219px}
.recipe-photo{height:120px}
.recipe-title{margin-top:13px;font-size:13px}
.recipe-excerpt{margin-top:7px;font-style:italic;font-size:8.6px;line-height:16px;padding-left:2px;padding-bottom:6px;border-bottom:1px solid var(--rule)}
.recipe-meta{margin-top:10px;font-size:7px;font-style:italic;line-height:16px;color:#444;display:flex;flex-wrap:wrap;align-items:center;gap:3px 7px}
.recipe-meta span{display:flex;align-items:center;gap:3px}

.about-title{left:150px;top:934px;font-size:19px}
.about-lead{left:150px;top:964px;font-size:11px;color:#333}
.about-text{left:150px;top:987px;width:340px;font-size:7.3px;line-height:12.8px}
.btn{left:150px;top:1082px;width:162px;height:34px;background:var(--red);color:var(--white);border-radius:2px;text-align:center;line-height:34px;font-family:"Roboto Condensed",sans-serif;font-size:13px;text-transform:uppercase}
.divider{left:507px;top:964px;width:1px;height:118px;background:var(--rule)}

.clients-title{left:534px;top:934px;font-size:19px}
.quote-mark{font-family:Georgia,serif;font-size:34px;color:#c8c8c8;line-height:1}
.client-heading{left:565px;top:979px;font-size:8.6px;font-weight:700;color:var(--red);text-transform:uppercase}
.client-photo{left:564px;top:999px;width:78px;height:73px;border:3px solid #e2e2e2;background:linear-gradient(160deg,#d9dcd8,#b7a08d)}
.client-text{left:658px;top:1003px;width:165px;font-size:7.6px;font-style:italic;line-height:13.6px}
.client-name{left:565px;top:1086px;font-size:8px;color:var(--red);text-transform:uppercase}
.client-date{left:565px;top:1100px;font-size:8px;font-style:italic}

.footer{left:0;top:1149px;width:993px;height:51px;background:var(--red);color:var(--white);font-size:6.8px;text-transform:uppercase}
.footer-nav{position:absolute;left:152px;top:20px;display:flex;align-items:center}
.footer-nav span{padding:0 12px;border-left:1px solid rgba(255,255,255,.8);line-height:8px}
.footer-nav span:first-child{padding-left:0;border-left:0}
.copyright{position:absolute;right:149px;top:20px}
</style>
</head>
<body>

<header>
  <div class="abs brand"><div class="brand-mark"></div><div class="brand-name">Bright Spoon Kitchen</div></div>
  <div class="abs follow"><span>FOLLOW US :</span>
    <i class="social"></i><i class="social"></i><i class="social"></i><i class="social alt"></i><i class="social"></i><i class="social alt"></i>
  </div>
</header>

<nav class="abs nav">
  <ul>
    <li class="active">Home</li>
    <li class="item" style="left:137px">About Us</li>
    <li class="item" style="left:252px">Services</li>
    <li class="item" style="left:365px">Products</li>
    <li class="item" style="left:484px">Features</li>
    <li class="item" style="left:600px">Contact Us</li>
  </ul>
</nav>

<section class="abs slider" role="img" aria-label="Bowl of noodles with seared beef, greens and red chilli">
  <div class="slider-arrow prev"><svg width="14" height="20"><path d="M12 1 L2 10 L12 19" fill="none" stroke="#fff" stroke-width="1"/></svg></div>
  <div class="slider-arrow next"><svg width="14" height="20"><path d="M2 1 L12 10 L2 19" fill="none" stroke="#fff" stroke-width="1"/></svg></div>
</section>

<h1 class="abs welcome-title section-title">Welcome to Bright Spoon Kitchen</h1>
<div class="abs double-rule"></div>
<p class="abs welcome-text">I'm a mother of a beautiful daughter who is now 16 months old at the time of writing.&nbsp; My kitchen experiments started not too long ago .. perhaps 2 years ago when I realize I was sick of eating out everyday. Back then it was just me and the hubby (otherwise known as Bubba in this blog) and cooking for 2 can be troublesome because we would be arguing over who should be doing the dishes.</p>

<h2 class="abs feature-title section-title">Feature our cooking recipes</h2>
<div class="abs pager" style="left:794px;top:630px">
  <i><svg width="13" height="6"><path d="M12 3H1M4 0.5L1 3L4 5.5" fill="none" stroke="#fff" stroke-width="0.8"/></svg></i>
  <i><svg width="13" height="6"><path d="M1 3H12M9 0.5L12 3L9 5.5" fill="none" stroke="#fff" stroke-width="0.8"/></svg></i>
</div>

<article class="abs recipe" style="left:150px">
  <div class="recipe-photo" role="img" aria-label="Grilled fish with roasted onion and rice" style="background:linear-gradient(135deg,#d7cfb9,#8a6a3c 55%,#5d6e35)"></div>
  <h3 class="recipe-title section-title">Banana Cake/Loaf</h3>
  <p class="recipe-excerpt">I'm a mother of a beautiful daughter who is now 16 months old at the time of writing....</p>
  <div class="recipe-meta"><span>◷ 15th September 2013</span><span>▬ Bakes</span><span>◆ banana cake, banana loaf</span><span>● Spoon Mama</span></div>
</article>
<article class="abs recipe" style="left:388px">
  <div class="recipe-photo" role="img" aria-label="Sliced banana loaf" style="background:linear-gradient(135deg,#c9c2b9,#a3714a 50%,#cfc6bc)"></div>
  <h3 class="recipe-title section-title">Banana Cake/Loaf</h3>
  <p class="recipe-excerpt">I'm a mother of a beautiful daughter who is now 16 months old at the time of writing....</p>
  <div class="recipe-meta"><span>◷ 15th September 2013</span><span>▬ Bakes</span><span>◆ banana cake, banana loaf</span><span>● Spoon Mama</span></div>
</article>
<article class="abs recipe" style="left:626px">
  <div class="recipe-photo" role="img" aria-label="Glazed chicken on rice with vegetables" style="background:linear-gradient(135deg,#9bb06a,#c0772c 50%,#e9e8e2)"></div>
  <h3 class="recipe-title section-title">Banana Cake/Loaf</h3>
  <p class="recipe-excerpt">I'm a mother of a beautiful daughter who is now 16 months old at the time of writing....</p>
  <div class="recipe-meta"><span>◷ 15th September 2013</span><span>▬ Bakes</span><span>◆ banana cake, banana loaf</span><span>● Spoon Mama</span></div>
</article>

<h2 class="abs about-title section-title">Who is Spoon Mama?</h2>
<p class="abs about-lead">Hi! Welcome to brightspoonkit.com</p>
<p class="abs about-text">I'm a mother of a beautiful daughter who is now 16 months old at the time of writing.&nbsp; My kitchen experiments started not too long ago .. perhaps 2 years ago when I realize I was sick of eating out everyday. Back then it was just me and the hubby (otherwise known as Bubba in this blog) and cooking for 2 can be troublesome because we would be arguing over who should be doing the dishes (him of course, since I was the one cooking!). Anyway, we both worked late so it didn't make sense for us to come back and whip up a meal, so we ate out a lot.</p>
<div class="abs btn">View our history</div>
<div class="abs divider"></div>

<h2 class="abs clients-title section-title">Happpy Clients</h2>
<div class="abs pager" style="left:794px;top:938px">
  <i><svg width="13" height="6"><path d="M12 3H1M4 0.5L1 3L4 5.5" fill="none" stroke="#fff" stroke-width="0.8"/></svg></i>
  <i><svg width="13" height="6"><path d="M1 3H12M9 0.5L12 3L9 5.5" fill="none" stroke="#fff" stroke-width="0.8"/></svg></i>
</div>
<div class="abs quote-mark" style="left:534px;top:964px">&ldquo;</div>
<div class="abs quote-mark" style="left:826px;top:1056px">&rdquo;</div>
<div class="abs client-heading">I'm a mother of a beautiful daughter</div>
<div class="abs client-photo" role="img" aria-label="Client portrait"></div>
<p class="abs client-text">I'm a mother of a beautiful daughter who is now 16 months old at the time of writing. My kitchen experiments started not too long ago .. perhaps 2 years ago when I realize .</p>
<div class="abs client-name">Marcus Ellery</div>
<div class="abs client-date">Posted on 28 Jul 2013</div>

<footer class="abs footer">
  <div class="footer-nav"><span>Home</span><span>About Us</span><span>Services</span><span>Products</span><span>Features</span><span>Contact Us</span></div>
  <div class="copyright">Copyright 2013. Bright Spoon Kitchen. All rights reserved.</div>
</footer>

</body>
</html>
```